Web Design for photo printing service

Hi
I am looking for a new web design theme for our almost ready website http://fotoblik.zrmq.net, it will soon be launched under the name: www.zuna.is. (ZUNA means: You Only Live Once)

This is a website focused on printing photo products like: photo books, Greeting cards, posters, etc.

The whole theme should be playful, fun, creative. The marketing will be is that Life is fun, keep your memories. remember the good time etc.

So what I am looking for is a simple, yet colorful theme, easy to use.

We will be running max 4- 6 product groups, all extra info should be on the button,
expect shopping chart and sign in should be on top.

Extra feature:
Once a year during christmas, the web will turn on christmas outfit, it transforms
to Christmas looking Web. So a X-mas version would be fun to see !

Target Market(s)

Young people 20-35, young families.

Industry/Entity Type

Printing

Requirements
Must have
• Fun looking colorful design, simple to use.
Should not have
• Dark heavy look

```html
<!DOCTYPE html>
<html lang="en">
<head>
<meta charset="utf-8">
<title>ZUNA – Photo printing</title>
<link rel="stylesheet" href="https://fonts.googleapis.com/css2?family=Oswald:wght@300;400&family=Anton&family=Arimo:wght@400;700&display=swap">
<style>
:root{
  --page:#ececec;--topbar:#333333;--orange:#f7941d;--dark:#2b2b2b;
  --teal:#1b9a7a;--pink:#ee1c77;--yellow:#fde05e;--red:#e8401c;
  --gold:#ffc20e;--ink:#222;--white:#fff;--cyan:#1aa3c9;
}
*{margin:0;padding:0;box-sizing:border-box}
html,body{width:1200px;height:1160px;overflow:hidden}
body{position:relative;background:var(--page);font-family:Arimo,Arial,sans-serif;color:var(--ink)}
.abs{position:absolute}
.topbar{left:0;top:0;width:1200px;height:38px;background:var(--topbar)}
.topbar-links{left:794px;top:8px;width:290px;font:400 17.5px Oswald,sans-serif;color:#eee;white-space:nowrap;letter-spacing:.2px}
.topbar-links span{margin:0 6px}
.brand{font:400 64px Oswald,sans-serif;color:var(--cyan);letter-spacing:4px;display:flex;align-items:center;gap:12px;white-space:nowrap}
.brand i{display:block;width:18px;height:18px;border-radius:50%;background:var(--pink)}
.cart{left:860px;top:58px;display:flex;align-items:center;gap:8px;font-size:14px;color:#333;white-space:nowrap}
.cart em{font-style:normal;color:#e0201c}
.cart b{display:block;width:40px;height:38px;background:linear-gradient(135deg,var(--gold),var(--orange));transform:skewY(-12deg);border-radius:3px}
.nav{left:587px;top:114px;width:509px;height:47px;background:var(--orange);border-radius:3px 3px 0 0;font:300 20px Oswald,sans-serif;color:var(--white)}
.nav a{position:absolute;top:0;height:47px;line-height:47px;white-space:nowrap;text-decoration:none;color:inherit}
.nav a.active{left:0;width:92px;background:var(--dark);text-align:center}
.slider{left:95px;top:161px;width:1001px;height:398px;background:var(--white);border:1px solid #ddd;box-shadow:0 12px 10px -8px rgba(0,0,0,.35)}
.slide-photo{left:9px;top:9px;width:710px;height:379px;background:linear-gradient(135deg,#6d6257,#9c9086 45%,#cfcac4 60%,#8b7f73)}
.dots{left:632px;top:366px;display:flex;gap:6px}
.dots i{width:15px;height:15px;border-radius:50%;background:#3d8c3f}
.dots i:first-child{background:var(--white)}
.slide-panel{left:719px;top:9px;width:272px;height:379px;background:var(--teal);color:var(--white);padding:14px 15px}
.slide-panel h2{font:300 29px/38px Oswald,sans-serif;margin-bottom:14px;white-space:nowrap}
.slide-panel p{font-size:14px;line-height:19px}
.btn-more{left:15px;top:241px;width:113px;height:27px;background:var(--red);font:300 16px/27px Oswald,sans-serif;padding:0 10px;clip-path:polygon(0 0,88% 0,100% 50%,88% 100%,0 100%);border-radius:3px;white-space:nowrap}
.btn-start{left:15px;top:279px;width:208px;height:48px;background:linear-gradient(var(--gold),#f5a800);color:#222;font:300 29px/48px Oswald,sans-serif;padding:0 19px;clip-path:polygon(0 0,87% 0,100% 50%,87% 100%,0 100%);border-radius:4px;white-space:nowrap}
.rule{left:95px;width:1001px;height:1px;background:#cfcfcf}
.motto{left:308px;top:602px;font:400 34px Anton,sans-serif;color:#555;letter-spacing:.5px;white-space:nowrap}
.cta{left:636px;top:601px;width:268px;height:48px;background:var(--pink);color:var(--white);font:300 29px/48px Oswald,sans-serif;padding-left:54px;clip-path:polygon(0 0,92% 0,100% 50%,92% 100%,0 100%);border-radius:3px;white-space:nowrap}
.card{top:669px;height:230px;background:var(--white);box-shadow:0 1px 3px rgba(0,0,0,.25)}
.card .pic{position:absolute;left:7px;top:7px;right:7px;height:177px}
.card .label{position:absolute;left:0;right:0;bottom:0;height:39px;background:#000;color:var(--white);font:300 19px/39px Oswald,sans-serif;padding-left:14px;display:flex;align-items:center;gap:12px;white-space:nowrap}
.card .label svg{flex:none}
.nav-arrow{top:749px;width:37px;height:37px;border-radius:50%;background:#1c1c1c;border:3px solid var(--white);box-shadow:0 1px 3px rgba(0,0,0,.4)}
.footer{left:0;top:916px;width:1200px;height:244px;background:var(--yellow)}
.legal{left:131px;top:121px;font-size:12.5px;line-height:20px;color:#111;white-space:nowrap}
.ftag{left:470px;height:22px;color:var(--white);font-size:14px;padding:3px 6px;clip-path:polygon(0 0,88% 0,100% 100%,0 100%);white-space:nowrap}
.flinks{left:475px;font-size:12px;color:#111;white-space:nowrap}
.bottom{left:94px;top:173px;width:1002px;height:71px;background:#000}
.pay-title{left:14px;top:11px;font-size:11px;color:var(--white)}
.pay{top:32px;height:25px;background:var(--white);border:1px solid #aaa;font:700 12px Arimo,sans-serif;color:#1c4f9c;display:flex;align-items:center;justify-content:center}
.social{top:1px;width:41px;height:62px;color:var(--white);font:700 9px Arimo,sans-serif;display:flex;align-items:center;justify-content:center;clip-path:polygon(0 0,100% 0,100% 88%,50% 100%,0 88%)}
</style>
</head>
<body>
<header>
  <div class="abs topbar"></div>
  <nav class="abs topbar-links">SIGN IN<span>|</span>GET STARTED<span>|</span>BLOG<span>|</span>HELP</nav>
  <div class="abs brand" style="left:108px;top:58px">ZUNA<i></i></div>
  <div class="abs cart"><b></b>SHOPPING CART : <em>0 items</em></div>
  <nav class="abs nav">
    <a class="active">HOME</a>
    <a style="left:103px">ABOUT US</a>
    <a style="left:203px">PRODUCTS</a>
    <a style="left:315px">OUR PRICE</a>
    <a style="left:424px">CONTACT</a>
  </nav>
</header>

<section class="abs slider">
  <div class="abs slide-photo" role="img" aria-label="Open photo book with black and white couple pictures lying on a wooden table"></div>
  <div class="abs dots"><i></i><i></i><i></i><i></i></div>
  <div class="abs slide-panel">
    <h2>PHOTO BOOKS</h2>
    <p>Your own photographs? Why? We know that your images deserve to be preserved. Even probably the best pictures in the world - so practically. You choose the front page, page masses, the size of the images and can add frames and all kinds. The book will then be printed, bound ...</p>
    <div class="abs btn-more">Read More</div>
    <div class="abs btn-start">GET STARTED</div>
  </div>
</section>

<div class="abs rule" style="top:593px"></div>
<div class="abs motto">YOU ONLY LIVE ONCE</div>
<svg class="abs" style="left:593px;top:612px" width="30" height="24" viewBox="0 0 30 24"><path d="M2 12h24M16 3l10 9-10 9" fill="none" stroke="#f7941d" stroke-width="4"/></svg>
<div class="abs cta">GET STARTED</div>
<div class="abs rule" style="top:655px"></div>

<section>
  <div class="abs card" style="left:123px;width:228px"><div class="pic" role="img" aria-label="Family looking at a photo book" style="background:linear-gradient(135deg,#b5643a,#d99a6c 50%,#e7b8b4)"></div><div class="label"><svg width="10" height="12"><path d="M2 1l6 5-6 5" fill="none" stroke="#fff" stroke-width="2.5"/></svg>PHOTO BOOKS</div></div>
  <div class="abs card" style="left:366px;width:229px"><div class="pic" role="img" aria-label="Printed desk calendar with colored pencils" style="background:linear-gradient(90deg,#5d3a66,#8a5f96 35%,#e9e6ea 60%,#f5f3f5)"></div><div class="label"><svg width="10" height="12"><path d="M2 1l6 5-6 5" fill="none" stroke="#fff" stroke-width="2.5"/></svg>CALENDAR</div></div>
  <div class="abs card" style="left:610px;width:228px"><div class="pic" role="img" aria-label="Printed photographs spread on an album" style="background:linear-gradient(135deg,#3a3a3a,#6e7d8c 50%,#c4c9cf)"></div><div class="label"><svg width="10" height="12"><path d="M2 1l6 5-6 5" fill="none" stroke="#fff" stroke-width="2.5"/></svg>PRINT PHOTOGRAPHS</div></div>
  <div class="abs card" style="left:853px;width:216px"><div class="pic" role="img" aria-label="Poster print of a smiling couple outdoors" style="background:linear-gradient(135deg,#4fa3b8,#9a8a7a 50%,#5b4a3f)"></div><div class="label"><svg width="10" height="12"><path d="M2 1l6 5-6 5" fill="none" stroke="#fff" stroke-width="2.5"/></svg>POSTERS</div></div>
  <div class="abs nav-arrow" style="left:94px"><svg width="31" height="31"><path d="M18 10l-6 5.5 6 5.5" fill="none" stroke="#fff" stroke-width="2.5"/></svg></div>
  <div class="abs nav-arrow" style="left:1059px"><svg width="31" height="31"><path d="M13 10l6 5.5-6 5.5" fill="none" stroke="#fff" stroke-width="2.5"/></svg></div>
</section>

<footer class="abs footer">
  <div class="abs brand" style="left:102px;top:8px">ZUNA<i></i></div>
  <div class="abs legal">Copyright © 2013. All rights reserved.<br>Terms Of Use |&nbsp; Terms Of Service &nbsp;|&nbsp; Privacy Policy</div>
  <div class="abs ftag" style="top:16px;width:127px;background:var(--pink)">PRODUCTS</div>
  <div class="abs flinks" style="top:41px">Prints | Cards | Modern Pop Cards | Photo Books | &nbsp;Calendars &nbsp;| &nbsp;Fun Stuff &nbsp;| Pricing</div>
  <div class="abs ftag" style="top:67px;width:127px;background:var(--teal)">OCCASIONS</div>
  <div class="abs flinks" style="top:92px">Weddings | &nbsp;Baby &amp; Kids &nbsp;| &nbsp;Graduation &nbsp;| &nbsp;Sports &nbsp;| &nbsp;Business Merchandise | Gift Codes | &nbsp;Film &nbsp;| &nbsp;DVD Archives</div>
  <div class="abs ftag" style="top:119px;width:131px;background:#000">INFORMATION</div>
  <div class="abs flinks" style="top:145px">About Us | Shipping Info | Contact Us</div>
  <div class="abs bottom">
    <div class="abs pay-title">Choose your payment Gateway</div>
    <div class="abs pay" style="left:14px;width:77px">Paynest</div>
    <div class="abs pay" style="left:92px;width:46px">Orbica</div>
    <div class="abs pay" style="left:139px;width:45px">Amplex</div>
    <div class="abs pay" style="left:185px;width:46px">Vorta</div>
    <div class="abs social" style="left:686px;background:#2e5a50">Tagly</div>
    <div class="abs social" style="left:728px;background:#2aa9e0">Chirpy</div>
    <div class="abs social" style="left:770px;background:#3b5998">Friendo</div>
    <div class="abs social" style="left:812px;background:#333">Plusio</div>
    <div class="abs social" style="left:854px;background:#e0508a">Dribla</div>
  </div>
</footer>
</body>
</html>
```